Banner Ad (and potentially other creative assets) designed for a crowdfunding/finance industry association business conference called the 3rd annual Canadian Pooltrade Forum scheduled for March 1 & 2, 2017.

The conference covers topics around fintech (financial technology), crowdfinance, venture funding markets, online crowdfunding models and alternative finance.

Some words and concepts for reference:
Fintech, Crowdfunding, crowdfinance, investment crowdfunding, securities based crowdfunding, equity crowdfunding, crowdsourcing, reward-based crowdfunding

Startups, small businesses, angel investing, venture capital, online alternative finance, private capital markets, global funding

The design should be fresh, innovative, and jump off the page with excitement around new opportunities for raising capital online for businesses but also a great channel for investors active in venture funding.

Attached are some images and conference banners we used the past for reference.

Links for reference:
Federated Backers Guild of Canada website (fbgcanada-example.org)
Canadian Pooltrade Forum (pooltradeforum-example.ca)
PeakCAPITAL 2016 (peakcapitalmeet-example.ca)

What: 3rd Annual Canadian Pooltrade Forum
Date: March 1 & 2, 2017
Location: Lumen Works Quarter (venue for Day 2 is TBD)
Hashtag: #PTF2017

Fintech Crowdfunding and Alternative Finance Markets
Where the rubber hits the road
Innovation | Entrepreneurship | Investors

Target Market(s)

Startups, scaleups and small businesses, retail investors, angel investors, venture capital, online alternative finance, private capital markets, global funding, international partnerships

Industry/Entity Type

Crowdfunding

Font styles to use
Sans Serif

Colors
9bcb3b
33a6d7
6b449b

Requirements
Must have
• What: 3rd Annual Canadian Pooltrade Forum
• Day 1: March 1, 2017
• Lumen Works Quarter
• Day 2: March 2, 2017
• Location TBD
• Fintech Crowdfunding and Alternative Finance Markets
• Innovation | Entrepreneurship | Investors
• #PTF2017
• The design should be fresh, vibrant, dynamic, innovative, tech orientated, and jump off the page with excitement around new opportunities for raising capital online for businesses but also a great channel for investors active in venture funding. This is about bringing emerging fintech and crowdfinance markets TO LIFE!
• Concepts of innovation, technology, finance
Nice to have
• Day 1: Education, Networking, Live Pitching, Exhibitor Showcase
• Day 2: Trade show, Workshops, Meetings, Networking Reception
• Crowd, collaborative, change, impact, Global or international, Transformation, moving forward (progress)

```html
<!DOCTYPE html>
<html lang="en">
<head>
<meta charset="utf-8">
<title>Canadian Pooltrade Forum – Banner</title>
<link rel="stylesheet" href="https://fonts.googleapis.com/css2?family=Roboto:ital,wght@0,400;0,700;0,900;1,900&display=swap">
<style>
  :root {
    --blue: #33a6d7;
    --green: #9bcb3b;
    --purple: #6b449b;
    --mist: #f2eeee;
    --white: #ffffff;
  }
  html, body {
    margin: 0;
    padding: 0;
    width: 1200px;
    height: 369px;
    overflow: hidden;
    background: var(--white);
  }
  .banner {
    position: relative;
    width: 1200px;
    height: 369px;
    overflow: hidden;
    font-family: "Roboto", Arial, sans-serif;
  }
  .banner__shapes { position: absolute; inset: 0; }
  .banner__text {
    position: absolute;
    margin: 0;
    white-space: nowrap;
    line-height: 1;
  }
  .event-edition {
    left: 21px;
    top: 9px;
    font-size: 15px;
    font-weight: 700;
    letter-spacing: 2px;
    color: var(--white);
  }
  .event-title {
    left: 20px;
    top: 31px;
    font-size: 44px;
    font-weight: 700;
    letter-spacing: 0.5px;
    color: var(--white);
  }
  .event-theme {
    left: 17px;
    top: 107px;
    font-size: 23px;
    font-weight: 900;
    font-style: italic;
    letter-spacing: 0.5px;
    color: var(--purple);
  }
  .pillar__icon { position: absolute; display: block; }
  .pillar__label {
    font-size: 38px;
    font-weight: 700;
    letter-spacing: 0.3px;
  }
  .icon-innovation { left: 42px; top: 160px; }
  .label-innovation { left: 117px; top: 168px; color: var(--blue); }
  .icon-entrepreneurship { left: 115px; top: 236px; }
  .label-entrepreneurship { left: 195px; top: 238px; color: var(--green); }
  .icon-investors { left: 187px; top: 299px; }
  .label-investors { left: 263px; top: 307px; color: var(--purple); }
  .event-date {
    left: 790px;
    width: 400px;
    top: 119px;
    text-align: center;
    font-size: 38px;
    font-weight: 700;
    color: var(--white);
  }
  .event-day {
    left: 748px;
    font-size: 19px;
    font-weight: 900;
    font-style: italic;
    letter-spacing: 0.3px;
    color: var(--purple);
    text-shadow: 1px 1px 2px rgba(0,0,0,0.25);
  }
  .event-day--one { top: 203px; }
  .event-day--two { top: 235px; }
  .event-hashtag {
    right: 26px;
    top: 303px;
    font-size: 46px;
    font-weight: 400;
    letter-spacing: 0.5px;
    color: var(--white);
  }
</style>
</head>
<body>
<div class="banner">
  <svg class="banner__shapes" width="1200" height="369" viewBox="0 0 1200 369" aria-hidden="true">
    <polygon points="0,0 868,0 605,369 0,369" fill="var(--mist)"/>
    <polygon points="0,0 868,0 802,92 0,92" fill="var(--blue)"/>
    <polygon points="802,92 1200,92 1200,183 738,183" fill="var(--green)"/>
    <polygon points="669,279 1200,279 1200,369 605,369" fill="var(--purple)"/>
  </svg>

  <p class="banner__text event-edition">3RD ANNUAL</p>
  <h1 class="banner__text event-title">CANADIAN POOLTRADE FORUM</h1>
  <p class="banner__text event-theme">FINTECH CROWDFUNDING AND ALTERNATIVE FINANCE MARKETS</p>

  <svg class="pillar__icon icon-innovation" width="46" height="52" viewBox="0 0 30 42" aria-hidden="true">
    <g stroke="var(--blue)" stroke-width="2" stroke-linecap="round">
      <line x1="15" y1="1" x2="15" y2="5"/>
      <line x1="3" y1="6" x2="6" y2="9"/>
      <line x1="27" y1="6" x2="24" y2="9"/>
      <line x1="0" y1="17" x2="3" y2="17"/>
      <line x1="27" y1="17" x2="30" y2="17"/>
    </g>
    <path d="M15 8a9 9 0 0 0-5 16.5V29h10v-4.5A9 9 0 0 0 15 8z" fill="var(--blue)"/>
    <rect x="10" y="31" width="10" height="3" rx="1" fill="var(--blue)"/>
    <rect x="11" y="36" width="8" height="3" rx="1.5" fill="var(--blue)"/>
  </svg>
  <span class="banner__text pillar__label label-innovation">INNOVATION</span>

  <svg class="pillar__icon icon-entrepreneurship" width="50" height="38" viewBox="0 0 46 34" aria-hidden="true">
    <rect x="1" y="2" width="30" height="22" fill="none" stroke="var(--green)" stroke-width="2.5"/>
    <rect x="7" y="14" width="4" height="7" fill="var(--green)"/>
    <rect x="14" y="10" width="4" height="11" fill="var(--green)"/>
    <rect x="21" y="7" width="4" height="14" fill="var(--green)"/>
    <circle cx="37" cy="15" r="5" fill="var(--green)"/>
    <path d="M28 34v-6a9 7 0 0 1 18 0v6z" fill="var(--green)"/>
  </svg>
  <span class="banner__text pillar__label label-entrepreneurship">ENTREPRENEURSHIP</span>

  <svg class="pillar__icon icon-investors" width="50" height="46" viewBox="0 0 50 44" aria-hidden="true">
    <circle cx="10" cy="5" r="4.5" fill="var(--purple)"/>
    <path d="M3 12h14v16h-3v16h-8V28H3z" fill="var(--purple)"/>
    <circle cx="35" cy="28" r="13" fill="none" stroke="var(--purple)" stroke-width="2.5"/>
    <text x="35" y="35" text-anchor="middle" font-family="Roboto, Arial, sans-serif" font-weight="700" font-size="19" fill="var(--purple)">$</text>
  </svg>
  <span class="banner__text pillar__label label-investors">INVESTORS</span>

  <p class="banner__text event-date">MARCH 1 &amp; 2, 2017</p>
  <p class="banner__text event-day event-day--one">DAY 1 · MARCH 1 · LUMEN WORKS QUARTER</p>
  <p class="banner__text event-day event-day--two">DAY 2 · MARCH 2 · LOCATION TBD</p>
  <p class="banner__text event-hashtag">#PTF2017</p>
</div>
</body>
</html>
```